2 banner Designs

I have a trade show in Vegas and I want you to design 2 banners that are Graphic size: 33.5" (W) x 80.5" (H). The banners are standing in the booth.

I am looking for a luxury modern feel for the banners. The banners are going to be important to attract customers in.

I am showing latex foam pillows and latex mattress. The company is called Verdant Hush. Please use any photos from our website.

https://www.loomvaleny.net/verdanthush

Banner 1

Introducing our Verdant Hush mattress, a perfect harmony of luxurious organic cushioning and an advanced internal, zoned pressure-point support system.

Experience unparalleled back support and remarkable durability, all in one exceptional sleep solution.

Verdant Hush Mattress

TerraWeave-certified organic cotton
TerraWeave-certified organic wool
2 “ PureSap-certified organic latex
8” Pocket Coils
1’’ PureSap-certified organic latex

Banner 2

Verdant Hush Pillows

We developed a customizable pillow with the perfect amount of comfort and support.

Our New Latex pillow has an adjustable fill with 90% Natural Latex and 10% Traceable Wool.  Our pillow cover is made from TerraWeave-certified organic cotton.

FILE REQUIREMENTS
We can take the file in the following file formats:

Single Page PDF (Preferred)
JPG (Preferred)
PSD – Please flatten file
EPS – Please embed all images. Outline all fonts and strokes.
Ai – Please embed all images. Outline all fonts and strokes.
Don't Include Crop Marks or Bleed

Artwork at either full scale, 1/2 scale or 1/10 scale that is fine. Just make sure that when the file is being set up the DPI is compensated according to the scale.

Full Scale – 150 DPI
1/2 Scale – 300 DPI
1/10 Scale – 450 DPI
***Remove EVERYTHING from your file that you do not want printed on the final product - especially hidden layers and template guidelines.

- Flatten all Objects/Gradients/Swatches/Symbols/Special Effects/Transparencies
- Outline all text
- Flattened PDF (Single Page) or JPEG file types only
- Remove all crop marks/bleed otherwise they will be printed
- File must be the same exact size as what is ordered (exception is Gallery wrap Fold Edge and Products with templates)
- CMYK only (we do not print Pantone/5th/Spot/RGB)
- 150 dpi
- If using a template, the file uploaded to our site should match the exact "template size" (different than "graphic size").
- Do not scale template files, just flatten them and save at 150 dpi
- Files over 200" can be scaled
- Under 300 mb for upload

- Make sure all objects are embedded and flattened (we do not print Non-Native Art).
- If the file is made in Indesign, please flatten the file in Illustrator or Photoshop and export to a JPEG ONLY as we don't recommend using Indesign at our facility.

- If using Compound Paths to create transparencies/shapes, please completely rasterize or flatten them into the file or they may print incorrectly.

- We do not have specific measurements for Panel jobs. If you are printing in Panels, please make sure you are providing a minimum of 1" overlay in your files.

Please make sure that your file is in CMYK format for print production with no bleed. It is not required.

```html
<!DOCTYPE html>
<html lang="en">
<head>
<meta charset="utf-8">
<title>Verdant Hush – Trade Show Banners</title>
<link href="https://fonts.googleapis.com/css2?family=Domine:wght@400;700&family=Poppins:wght@400;500;600;700&display=swap" rel="stylesheet">
<style>
  :root{
    --green:#678c22;
    --olive-dark:#4b4a3c;
    --tan:#c8cb9c;
    --ink:#3a3a36;
    --rule:#6b6b63;
    --paper:#ffffff;
    --backdrop:#ffffff;
  }
  *{margin:0;padding:0;box-sizing:border-box}
  html,body{width:1200px;height:2768px;overflow:hidden}
  body{background:var(--backdrop);position:relative;font-family:"Poppins",sans-serif;color:var(--ink)}
  .banner{position:absolute;top:1416px;width:462px;height:1111px;background:var(--paper);box-shadow:0 4px 14px rgba(0,0,0,.25);overflow:hidden}
  .banner--mattress{left:107px}
  .banner--pillows{left:649px}
  .abs{position:absolute;left:0;width:100%}
  .brand{top:112px;text-align:center;font-family:"Domine",serif;font-weight:400;font-size:38px;line-height:46px;color:var(--green)}
  .brand-dot{display:inline-block;width:14px;height:14px;border-radius:50%;background:var(--green);margin-right:10px;vertical-align:middle;position:relative;top:-3px}
  .photo{position:absolute;left:43px;top:206px;width:376px;height:202px}
  .headline{font-family:"Domine",serif;font-weight:700;text-align:center}
  .headline .g{color:var(--green)} .headline .d{color:var(--olive-dark)}
  .headline--mattress{top:422px;font-size:42px;line-height:46px}
  .headline--pillows{top:416px;font-size:70px;line-height:65px;letter-spacing:-1px}
  .dots{display:flex;justify-content:center;gap:5px}
  .dots span{width:10px;height:8px;background:var(--olive-dark)}
  .dots span:last-child{background:var(--tan)}
  .lead{text-align:center;color:var(--ink)}
  .rule{position:absolute;left:43px;width:376px;height:1.5px;background:var(--rule)}
  .certs{position:absolute;left:43px;top:676px;width:376px;height:98px;display:flex}
  .cert{flex:1;display:flex;flex-direction:column;align-items:center;border-left:1.5px solid var(--rule)}
  .cert:first-child{border-left:none}
  .cert-badge-round{width:56px;height:56px;border-radius:50%;background:var(--green);margin-top:8px}
  .cert-badge-tag{width:80px;height:48px;border-radius:6px;background:var(--green);margin-top:12px}
  .cert-caption{position:absolute;top:76px;font-size:7.5px;font-weight:600;line-height:9px;text-align:center;color:var(--ink)}
  .cert{position:relative}
  .claim{top:790px;font-family:"Domine",serif;font-weight:700;font-size:19px;line-height:21px;text-align:center;color:var(--ink)}
  .ribbon{position:absolute;left:59px;top:891px;width:345px;height:56px}
  .ribbon-label{position:absolute;left:0;width:100%;top:905px;line-height:28px;text-align:center;font-family:"Domine",serif;font-size:20px;color:#fff}
  .footer{position:absolute;left:0;top:982px;width:100%;height:129px;background:var(--green);border-radius:24px 24px 0 0}
  .phone{position:absolute;left:65px;top:965px;width:320px;height:71px;border-radius:36px;background:var(--olive-dark);color:#fff;font-weight:600;font-size:42px;text-align:center;line-height:72px}
  .url{top:1051px;text-align:center;color:#fff;font-weight:600;font-size:16px;line-height:22px;letter-spacing:.8px}
  .fill-intro{top:732px;left:43px;width:376px;font-size:15px;line-height:22px;color:var(--ink)}
  .stats{position:absolute;left:43px;top:758px;width:376px;height:50px;display:flex;align-items:center}
  .stat-num{font-weight:700;font-size:42px;color:var(--green);line-height:1}
  .stat-label{font-size:15px;line-height:16px;margin-left:9px;color:var(--ink)}
  .stat-divider{width:1.5px;height:46px;background:var(--rule);margin:0 10px}
  .cover{position:absolute;left:43px;top:838px;width:376px;height:100px;display:flex;align-items:center}
  .cover .cert-badge-round{width:98px;height:98px;margin:0 24px 0 0;flex:none}
  .cover p{font-size:19px;line-height:24px;color:var(--ink)}
</style>
</head>
<body>

<section class="banner banner--mattress">
  <div class="abs brand"><span class="brand-dot"></span>Verdant Hush</div>
  <svg class="photo" viewBox="0 0 450 240" preserveAspectRatio="none" role="img" aria-label="Photo of a smiling woman sitting on a bed hugging a latex pillow, wooden headboard behind">
    <defs><linearGradient id="pm" x1="0" y1="0" x2="0" y2="1"><stop offset="0" stop-color="#d9cbb8"/><stop offset=".45" stop-color="#a8744d"/><stop offset="1" stop-color="#ebe6de"/></linearGradient></defs>
    <path d="M0,0 H200 Q225,0 225,30 Q225,0 250,0 H450 V130 Q450,240 345,240 H245 Q225,240 225,215 Q225,240 205,240 H105 Q0,240 0,130 Z" fill="url(#pm)"/>
  </svg>
  <h1 class="abs headline headline--mattress"><span class="g">Introducing</span><br><span class="d">Our Verdant</span><br><span class="g">Hush Mattress</span></h1>
  <div class="abs dots" style="top:567px"><span></span><span></span><span></span><span></span></div>
  <p class="abs lead" style="top:590px;font-size:17px;line-height:20.5px;padding:0 34px">a perfect harmony of luxurious organic cushioning and an advanced internal, zoned pressure-point support system.</p>
  <div class="rule" style="top:669px"></div>
  <div class="certs">
    <div class="cert"><div class="cert-badge-round"></div><p class="cert-caption">TerraWeave-certified<br>organic cotton</p></div>
    <div class="cert"><div class="cert-badge-round"></div><p class="cert-caption">TerraWeave-certified<br>organic wool</p></div>
    <div class="cert"><div class="cert-badge-tag"></div><p class="cert-caption">2 PureSap-certified<br>organic latex</p></div>
    <div class="cert"><div class="cert-badge-tag"></div><p class="cert-caption">1 PureSap-certified<br>organic latex</p></div>
  </div>
  <div class="rule" style="top:779px"></div>
  <p class="abs claim">Experience unparalleled back<br>support and remarkable durability,<br>all in one exceptional sleep solution.</p>
  <div class="rule" style="top:870px;left:59px;width:345px"></div>
  <svg class="ribbon" viewBox="0 0 345 56" preserveAspectRatio="none" aria-hidden="true"><path d="M0,0 H345 L330,28 L345,56 H0 L15,28 Z" fill="var(--green)"/></svg>
  <div class="ribbon-label">Verdant Hush Mattress</div>
  <div class="footer"></div>
  <div class="phone">555.014.2270</div>
  <p class="abs url">www.loomvaleny.net/verdanthush</p>
</section>

<section class="banner banner--pillows">
  <div class="abs brand"><span class="brand-dot"></span>Verdant Hush</div>
  <svg class="photo" viewBox="0 0 450 240" preserveAspectRatio="none" role="img" aria-label="Photo of a woman in a rust pajama set lying on a bed resting on a white latex pillow">
    <defs><linearGradient id="pp" x1="0" y1="0" x2="1" y2="1"><stop offset="0" stop-color="#5c4a3e"/><stop offset=".4" stop-color="#a9684d"/><stop offset="1" stop-color="#ece8e1"/></linearGradient></defs>
    <path d="M0,0 H200 Q225,0 225,30 Q225,0 250,0 H450 V130 Q450,240 345,240 H245 Q225,240 225,215 Q225,240 205,240 H105 Q0,240 0,130 Z" fill="url(#pp)"/>
  </svg>
  <h1 class="abs headline headline--pillows"><span class="g">Verdant</span><br><span class="d">Hush</span><br><span class="g">Pillows</span></h1>
  <div class="abs dots" style="top:624px"><span></span><span></span><span></span><span></span></div>
  <p class="abs lead" style="top:642px;font-size:17px;line-height:19.5px;padding:0 64px">We developed a customizable pillow with the perfect amount of comfort and support.</p>
  <div class="rule" style="top:722px"></div>
  <p class="abs fill-intro">Our New Latex pillow has an adjustable fill with</p>
  <div class="stats">
    <span class="stat-num">90%</span><span class="stat-label">Natural<br>Latex and</span>
    <span class="stat-divider"></span>
    <span class="stat-num">10%</span><span class="stat-label">Traceable<br>Wool</span>
  </div>
  <div class="rule" style="top:820px"></div>
  <div class="cover">
    <div class="cert-badge-round"></div>
    <p>Our pillow cover is made<br>from TerraWeave-certified<br>organic cotton.</p>
  </div>
  <div class="footer"></div>
  <div class="phone">555.014.2270</div>
  <p class="abs url">www.loomvaleny.net/verdanthush</p>
</section>

</body>
</html>
```